Stationery Design Project - Professional Training Company

Full set of statinery in PDF and format that can be given to the printers

Letterhead
Business cards x 3
Compliments slip
Envelope
Updates

Many thanks for all your contributions, the quality of the designs is amazing.

Thank you all so much for your contribution to this project, I am very impressed with the designs and choice of designs, you are all clearly very talented individuals.

I hope to be making a decision on the final choice this evening UAE time.

Best regards and again thank you so much

Desmond

I would like to take this opportunity to thank you all for your contributions, I have been very impressed with each of the designs submitted.

I will shortly go back and give each of you a personal rating on each of your designs.

Again thank you all so much for your efforts

Best Regards

Desmond

Target Market(s)

We are a training company that provides IT training for Medical and Professional Staff, we train professional adults

Industry/Entity Type

Business

Requirements
Must have
• The letterhead and compliments slip must have at the bottom of the page:-

Bright Harbor Learning LLP operates as a limited liability partnership registered in England and Wales (with registered number OC742168)

Business Cards are to be made up for three people (details of those to be provided after appoval of design but are included in this project) and should contain:

Name
Title
Telephone
email
Address: P.O. Box 518243 Dubai UAE
web address: www.brightharborlearning.example
Nice to have
• Very clean and professional looking
Should not have
• No look to busy or ovr crowded

```html
<!DOCTYPE html>
<html lang="en">
<head>
<meta charset="utf-8">
<title>Bright Harbor Learning LLP – Business Card</title>
<link rel="stylesheet" href="https://fonts.googleapis.com/css2?family=Ubuntu:wght@400;500&display=swap">
<style>
  :root {
    --page-bg: #eceff2;
    --card-bg: #ffffff;
    --ink: #2a1f2d;
    --ink-soft: #3b3340;
    --accent-purple: #8e2a7c;
    --accent-green: #4f9a2a;
    --card-shadow: rgba(20, 40, 60, 0.14);
  }
  * { box-sizing: border-box; margin: 0; padding: 0; }
  html, body {
    width: 1200px;
    height: 797px;
    overflow: hidden;
  }
  body {
    background: var(--page-bg);
    font-family: "Ubuntu", "Segoe UI", sans-serif;
    color: var(--ink);
    display: flex;
    align-items: center;
    justify-content: center;
    gap: 40px;
  }
  .business-card {
    position: relative;
    width: 540px;
    height: 310px;
    background: var(--card-bg);
    box-shadow: 0 10px 28px var(--card-shadow), 0 2px 4px var(--card-shadow);
  }

  /* Front */
  .card-front {
    display: flex;
    align-items: center;
    justify-content: center;
  }
  .brand-lockup {
    display: flex;
    align-items: center;
    gap: 16px;
  }
  .brand-dot {
    width: 44px;
    height: 44px;
    border-radius: 50%;
    background: var(--accent-purple);
  }
  .brand-name {
    font-size: 26px;
    font-weight: 400;
    color: var(--ink);
    letter-spacing: -0.2px;
  }

  /* Back */
  .card-back .brand-dot {
    position: absolute;
    top: 38px;
    left: 42px;
    width: 40px;
    height: 40px;
  }
  .contact-block {
    position: absolute;
    left: 232px;
    top: 118px;
  }
  .contact-rule {
    width: 30px;
    height: 2px;
    background: var(--accent-purple);
    margin-bottom: 9px;
  }
  .person-name {
    font-size: 17px;
    font-weight: 500;
    color: var(--ink);
    line-height: 1.1;
  }
  .person-title {
    font-size: 11.5px;
    color: var(--ink-soft);
    margin-bottom: 14px;
  }
  .contact-line {
    font-size: 11.5px;
    color: var(--ink-soft);
    line-height: 1.5;
  }
  .contact-web {
    color: var(--accent-purple);
  }
</style>
</head>
<body>
  <section class="business-card card-front" aria-label="Business card front">
    <div class="brand-lockup">
      <span class="brand-dot" aria-hidden="true"></span>
      <span class="brand-name">Bright Harbor Learning LLP</span>
    </div>
  </section>

  <section class="business-card card-back" aria-label="Business card back">
    <span class="brand-dot" aria-hidden="true"></span>
    <div class="contact-block">
      <div class="contact-rule"></div>
      <p class="person-name">Leona Marsh</p>
      <p class="person-title">Operation Manager</p>
      <p class="contact-line">(221) 47 260 18 35</p>
      <p class="contact-line">name@brightharborlearning.example</p>
      <p class="contact-line">P.O. Box 518243 Dubai UAE</p>
      <p class="contact-line contact-web">www.brightharborlearning.example</p>
    </div>
  </section>
</body>
</html>
```